terras letterhead

We would like to create a new letterhead that our company will use for proposals, invoices, statements and letters. Our company name is Terra-Vantage. We are a landscape design/build and landscape maintenance company. We have a web site Terra-Vantage.example where our logo (the leaf with the lettering within it only) is displayed.

Industry/Entity Type

Graphic Design

Requirements
Must have
• Address and info on our current letterhead (uploaded)
Nice to have
• We would like the design to look presentable in grey scale as well as color.
Should not have
• Do not want to infringe much on the normal useable area within the normal print areas.

```html
<!DOCTYPE html>
<html lang="en">
<head>
<meta charset="utf-8">
<title>Terra-Vantage Letterhead</title>
<link href="https://fonts.googleapis.com/css2?family=Tinos:wght@400;700&display=swap" rel="stylesheet">
<style>
  :root {
    --frame: #e6e6e6;
    --backdrop: #59595b;
    --paper: #ffffff;
    --forest: #1f3f23;
    --ink-green: #1f4a25;
  }
  * { margin: 0; padding: 0; box-sizing: border-box; }
  html, body {
    width: 1200px;
    height: 1000px;
    overflow: hidden;
    background: var(--frame);
  }
  .backdrop {
    position: absolute;
    left: 9px; top: 9px;
    width: 1182px; height: 982px;
    background: var(--backdrop);
  }
  .letterhead {
    position: absolute;
    left: 294px; top: 84px;
    width: 602px; height: 846px;
    background: var(--paper);
    box-shadow: 6px 10px 18px rgba(0,0,0,0.45);
    font-family: "Tinos", "Times New Roman", serif;
    color: var(--ink-green);
  }
  .side-band {
    position: absolute;
    left: 0; top: 0;
    width: 24px; height: 100%;
    background: var(--forest);
  }
  .company-name {
    position: absolute;
    left: 40px; top: 28px;
    font-size: 21px;
    font-weight: 700;
    letter-spacing: 0.5px;
    color: var(--forest);
  }
  .contact-block {
    position: absolute;
    right: 35px; top: 12px;
    text-align: right;
    font-size: 10.5px;
    line-height: 14px;
  }
  .web-address {
    position: absolute;
    left: 0; right: 0;
    bottom: 13px;
    text-align: center;
    font-size: 11px;
  }
</style>
</head>
<body>
  <div class="backdrop"></div>
  <div class="letterhead">
    <div class="side-band"></div>
    <div class="company-name">Terra-Vantage</div>
    <address class="contact-block" style="font-style:normal">
      <div class="contact-line">T: (555) 010-1155</div>
      <div class="contact-line">E: service@terra-vantage.example</div>
      <div class="contact-line">F: (555) 010-7820</div>
      <div class="contact-line">A: 48 Meadowbrook Lane Fernhill, NJ 07000</div>
    </address>
    <div class="web-address">www.terra-vantage.example</div>
  </div>
</body>
</html>
```